OurPlume Lifting Hope across a trusted circle

I am looking for a sleek, clean and simple app design. I need also a payment page and offering different packages and payment types.

I would like the color scheme to be black or white very futuristic like the movie q-lantern.

The profile page displaying the picture, as clean and future like as possible.

Share profile options, manage subscription, update profile, help ect….

On the verified page last one, the social media logos are interactive so the user can share their info through the connected social media account.

Target Market(s)

Professionals and individuals.

Industry/Entity Type

Due diligence & background checks verification

Font styles to use
Sans Serif

Colors
0054AA
0677BA
7BADD7
CADEEF
E8F1F8
0094D4
00A9DD
6FCCEA
C7EBF8
E9F6FB
59FF00
82FF00
B8FF75
E3FFCB
F4FFEA

Requirements
Must have
• The ability to add my social media links or log in through the app directly for direct confirmation. After email entered on account sign up they get either a confirmation email or a text through telephone number verification.
Nice to have
• Account creation to add profile picture must take a selfie.

```html
<!DOCTYPE html>
<html lang="en">
<head>
<meta charset="utf-8">
<title>OurPlume – Sign up and Sign in</title>
<link rel="stylesheet" href="https://fonts.googleapis.com/css2?family=Nunito:wght@400;600;700;800&display=swap">
<style>
  :root {
    --navy: #1f3278;
    --brand-blue: #0054aa;
    --sky: #7badd7;
    --mist: #cadeef;
    --ice: #e8f1f8;
    --cyan: #6fccea;
    --white: #ffffff;
    --glass: rgba(205, 222, 250, 0.42);
    --glass-edge: rgba(255, 255, 255, 0.7);
    --hint: rgba(255, 255, 255, 0.8);
    --alert: #ff6a52;
    --scene-top: #aabce0;
    --scene-mid: #7a90c2;
    --scene-low: #2c3f72;
    --scene-floor: #1a2a55;
  }
  * { box-sizing: border-box; margin: 0; padding: 0; }
  html, body { width: 1200px; height: 811px; overflow: hidden; }
  body { font-family: "Nunito", sans-serif; background: var(--scene-low); }

  .stage { position: relative; width: 1200px; height: 811px; overflow: hidden; }

  .backdrop {
    position: absolute; inset: 0;
    background:
      radial-gradient(ellipse 260px 300px at 900px 220px, rgba(30, 45, 95, 0.55), transparent 70%),
      radial-gradient(ellipse 200px 260px at 200px 380px, rgba(30, 45, 95, 0.45), transparent 70%),
      linear-gradient(180deg, var(--scene-top) 0%, var(--scene-mid) 48%, var(--scene-low) 72%, var(--scene-floor) 100%);
  }

  .screen {
    position: absolute; top: 198px; width: 211px; height: 458px;
    border-radius: 36px;
    background: var(--glass);
    border: 1px solid var(--glass-edge);
    backdrop-filter: blur(8px);
    box-shadow: 0 10px 30px rgba(20, 35, 80, 0.25);
    color: var(--white);
  }
  .screen--username { left: 228px; }
  .screen--details  { left: 476px; }
  .screen--signin   { left: 733px; }

  .brand {
    position: absolute; top: 48px; left: 0; width: 100%;
    display: flex; align-items: center; justify-content: center; gap: 6px;
  }
  .brand__dot { width: 14px; height: 14px; border-radius: 50%; background: var(--cyan); }
  .brand__name { font-size: 19px; font-weight: 800; color: var(--navy); letter-spacing: 0.5px; }

  .step-title { position: absolute; left: 20px; top: 124px; font-size: 8.5px; font-weight: 700; }

  .stepper { position: absolute; top: 143px; left: 20px; width: 168px; height: 36px; }
  .stepper__link {
    position: absolute; top: 17px; height: 0;
    border-top: 1px dashed rgba(255, 255, 255, 0.7);
  }
  .stepper__link--a { left: 37px; width: 30px; }
  .stepper__link--b { left: 103px; width: 29px; }
  .stepper__dot {
    position: absolute; top: 0; width: 36px; height: 36px; border-radius: 50%;
    background: rgba(236, 243, 255, 0.8);
    border: 1px solid var(--glass-edge);
    box-shadow: inset 0 0 0 4px rgba(255, 255, 255, 0.45), 0 2px 6px rgba(40, 60, 120, 0.18);
    display: flex; align-items: center; justify-content: center;
    font-size: 13px; font-weight: 600; color: var(--sky);
  }
  .stepper__dot--1 { left: 0; }
  .stepper__dot--2 { left: 66px; }
  .stepper__dot--3 { left: 131px; }
  .stepper__dot--current { color: var(--brand-blue); box-shadow: inset 0 0 0 4px rgba(255,255,255,0.55), 0 0 0 1px var(--sky); }
  .stepper__dot--active { color: var(--cyan); font-weight: 800; }

  .field {
    position: absolute; left: 20px; width: 168px; height: 33px;
    border-radius: 17px; border: 1px solid var(--glass-edge);
    background: rgba(255, 255, 255, 0.08);
    padding-left: 15px; display: flex; align-items: center;
    font-size: 8.5px; font-weight: 700;
  }
  .field__date { margin-left: auto; margin-right: 8px; font-size: 7.5px; display: flex; gap: 5px; align-items: center; }
  .field__date i { font-style: normal; font-size: 11px; font-weight: 400; }

  .prompt { position: absolute; left: 20px; top: 238px; font-size: 8.5px; font-weight: 700; }
  .prompt em { font-style: normal; color: var(--brand-blue); }

  .rules { position: absolute; left: 20px; top: 324px; list-style: none; font-size: 7px; font-weight: 600; line-height: 14.5px; }
  .rules li::before { content: "*"; color: var(--alert); margin-right: 2px; }

  .helper { position: absolute; left: 12px; width: 184px; text-align: center; font-size: 7.5px; line-height: 10px; color: var(--hint); white-space: nowrap; }
  .helper--top { top: 193px; }
  .helper--privacy { top: 370px; font-size: 7px; line-height: 8.5px; color: rgba(255,255,255,0.9); }
  .helper a { color: var(--brand-blue); font-weight: 700; text-decoration: underline; }

  .age-note { position: absolute; right: 22px; top: 346px; font-size: 7.5px; font-weight: 700; color: var(--alert); }

  .action {
    position: absolute; top: 402px; right: 23px; height: 33px;
    border-radius: 17px; border: 1px solid var(--glass-edge);
    display: flex; align-items: center; justify-content: center; gap: 10px;
    font-size: 8px; font-weight: 700; color: var(--white);
  }
  .action--next { width: 73px; }
  .action--join { width: 82px; }
  .action svg { width: 12px; height: 12px; }

  .signin-title { position: absolute; left: 25px; top: 110px; font-size: 24px; font-weight: 700; }

  .field--email { top: 191px; flex-direction: column; align-items: flex-start; justify-content: center; padding-left: 15px; }
  .field__label { font-size: 6.5px; font-weight: 700; }
  .field__value { font-size: 12px; font-weight: 700; color: var(--navy); margin-left: 12px; margin-top: 1px; }
  .field--password { top: 247px; }

  .forgot { position: absolute; right: 23px; top: 290px; font-size: 5.5px; font-weight: 700; text-decoration: underline; letter-spacing: 0.3px; }

  .power {
    position: absolute; left: 20px; top: 318px; width: 64px; height: 64px; border-radius: 50%;
    background: radial-gradient(circle at 40% 35%, var(--white), var(--ice));
    box-shadow: 0 6px 18px rgba(30, 50, 110, 0.3);
    display: flex; align-items: center; justify-content: center;
  }
  .power svg { width: 30px; height: 30px; }
</style>
</head>
<body>
<main class="stage">
  <div class="backdrop" role="img" aria-label="Hazy blue city scene with two large robots standing on a misty street"></div>

  <section class="screen screen--username">
    <div class="brand"><span class="brand__dot"></span><span class="brand__name">OurPlume</span></div>
    <p class="step-title">User Name</p>
    <div class="stepper">
      <span class="stepper__link stepper__link--a"></span>
      <span class="stepper__link stepper__link--b"></span>
      <span class="stepper__dot stepper__dot--1 stepper__dot--current">1</span>
      <span class="stepper__dot stepper__dot--2">2</span>
      <span class="stepper__dot stepper__dot--3">3</span>
    </div>
    <p class="prompt">Create a unique <em>OurPlume</em> username</p>
    <div class="field" style="top:259px;">Username</div>
    <ul class="rules">
      <li>Must be 3 to 20 characters long.</li>
      <li>Letter and numbers only.</li>
      <li>Spcial characters and spaces are not vaild.</li>
    </ul>
    <div class="action action--next">Next
      <svg viewBox="0 0 12 12"><path d="M1 6h10M6.5 1.5 11 6l-4.5 4.5" fill="none" stroke="currentColor" stroke-width="1.4"/></svg>
    </div>
  </section>

  <section class="screen screen--details">
    <div class="brand"><span class="brand__dot"></span><span class="brand__name">OurPlume</span></div>
    <p class="step-title">Details</p>
    <div class="stepper">
      <span class="stepper__link stepper__link--a"></span>
      <span class="stepper__link stepper__link--b"></span>
      <span class="stepper__dot stepper__dot--1 stepper__dot--active">1</span>
      <span class="stepper__dot stepper__dot--2">2</span>
      <span class="stepper__dot stepper__dot--3">3</span>
    </div>
    <p class="helper helper--top">Enter your first/Last name and date of birth<br>as it appears on your goverment issued ID</p>
    <div class="field" style="top:223px;">First Name</div>
    <div class="field" style="top:266px;">Last Name</div>
    <div class="field" style="top:310px;">Date of Birth
      <span class="field__date">DD <i>/</i> MM <i>/</i> YYYY</span>
    </div>
    <p class="age-note">Must be 18 years old or older</p>
    <p class="helper helper--privacy">We are committed to ensuring the privacy of<br>of your information. Please see our <a>Privacy Policy</a></p>
    <div class="action action--next">Next
      <svg viewBox="0 0 12 12"><path d="M1 6h10M6.5 1.5 11 6l-4.5 4.5" fill="none" stroke="currentColor" stroke-width="1.4"/></svg>
    </div>
  </section>

  <section class="screen screen--signin">
    <div class="brand"><span class="brand__dot"></span><span class="brand__name">OurPlume</span></div>
    <h1 class="signin-title">Sign in</h1>
    <div class="field field--email">
      <span class="field__label">Email Address</span>
      <span class="field__value">Mira Talvenhart</span>
    </div>
    <div class="field field--password">Password</div>
    <p class="forgot">FORGOT PASSWORD?</p>
    <div class="power">
      <svg viewBox="0 0 30 30"><path d="M9 9.5a9 9 0 1 0 12 0" fill="none" stroke="#9fb3d3" stroke-width="1.6" stroke-linecap="round"/><path d="M15 4v10" stroke="#9fb3d3" stroke-width="1.6" stroke-linecap="round"/></svg>
    </div>
    <div class="action action--join">Join Now
      <svg viewBox="0 0 12 12"><path d="M1 6h10M6.5 1.5 11 6l-4.5 4.5" fill="none" stroke="currentColor" stroke-width="1.4"/></svg>
    </div>
  </section>
</main>
</body>
</html>
```